Stonelynk Business Card Design

The Stonelynk Co is an aggregate (crushing) equipment dealer serving Western Canadian provinces. Stonelynk is a distributor of aggregate equipment for different manufacturers.

We are looking to change and update the existing business card which has been used since the existence of the company. A copy of existing card has been attached for reference. The Stonelynk Co logo we want to remain the same and we want the green color to remain the same.

We are wanting something new with a different look. A refreshing card to show a new modern and updated look. No longer wanting to have the manufacturers on the back of the card but something more like our logo on the back of the card with a statement like "Crushing Solutions"

ideas could be:
- card can be different colors on front and back
- front or reverse of the card could possibly be the green color with the logo in black

Target Market(s)

Owners of Aggregate/Crushing companies

Requirements
Must have
• - logo to remain same along with same font within logo
• - green color to remain same
Nice to have
• as noted above under project description
Should not have

```html
<!DOCTYPE html>
<html lang="en">
<head>
<meta charset="utf-8">
<title>Stonelynk Co – Business Card</title>
<link rel="stylesheet" href="https://fonts.googleapis.com/css2?family=Open+Sans:wght@300;700&display=swap">
<style>
  :root {
    --page: #ffffff;
    --ink: #000000;
    --olive: #8a8a35;
    --olive-text: #8a8a35;
  }
  * { box-sizing: border-box; margin: 0; padding: 0; }
  html, body {
    width: 1200px; height: 1000px; overflow: hidden;
    background: var(--page);
    font-family: "Open Sans", "Segoe UI", Arial, sans-serif;
  }
  .canvas { position: relative; width: 1200px; height: 1000px; }

  /* Front side */
  .card-front {
    position: absolute; left: 263px; top: 53px;
    width: 695px; height: 397px;
    background: var(--ink);
  }
  .tagline {
    position: absolute; left: 160px; top: 186px;
    color: var(--olive-text);
    font-weight: 300; font-size: 17px; letter-spacing: 9.4px;
    white-space: nowrap;
  }
  .company-name {
    position: absolute; left: 57px; top: 284px;
    color: var(--olive-text);
    font-weight: 700; font-size: 45px; letter-spacing: 0.5px;
    line-height: 1; white-space: nowrap;
  }

  /* Back side */
  .card-back {
    position: absolute; left: 263px; top: 527px;
    width: 697px; height: 398px;
    background: var(--olive);
  }
  .name-band {
    position: absolute; left: 0; top: 0;
    width: 100%; height: 111px;
    background: var(--ink);
  }
  .person-name {
    position: absolute; right: 42px; top: 38px;
    color: var(--olive-text);
    font-weight: 700; font-size: 30px; line-height: 1;
    white-space: nowrap;
  }
  .contact {
    position: absolute; right: 42px;
    color: var(--ink);
    font-weight: 700; font-size: 17.5px; line-height: 24px;
    text-align: right; white-space: nowrap;
  }
  .contact-address { top: 126px; }
  .contact-phones { top: 183px; }
  .contact-phones .line { display: flex; justify-content: flex-end; align-items: center; gap: 16px; }
  .contact-phones svg { width: 13px; height: 13px; }
  .contact-web { top: 321px; }

  .brand-mark {
    position: absolute; left: 42px; top: 248px;
    display: flex; align-items: center; gap: 14px;
    color: var(--ink);
    font-weight: 700; font-size: 30px; line-height: 1;
    white-space: nowrap;
  }
  .brand-dot {
    width: 34px; height: 34px; border-radius: 50%;
    background: var(--ink);
  }
</style>
</head>
<body>
<div class="canvas">

  <section class="card-front">
    <p class="tagline">Crushing Solutions</p>
    <h1 class="company-name">THE STONELYNK CO.</h1>
  </section>

  <section class="card-back">
    <div class="name-band">
      <h2 class="person-name">DALE MERCER</h2>
    </div>

    <div class="contact contact-address">
      <div>2280 - 48B Street</div>
      <div>Nisku, Alberta T9E 1R6</div>
    </div>

    <div class="contact contact-phones">
      <div class="line">
        <svg viewBox="0 0 16 16" aria-label="Phone" role="img">
          <path d="M4 1.5 C2 2.5 1.5 5 3 8 C4.5 11 7 13.5 10 14.5 C12 15 13.5 14 14.5 12.5 L11.5 10 L9.8 11.3 C8 10.5 5.5 8 4.7 6.2 L6 4.5 Z" fill="none" stroke="#000" stroke-width="1.3"/>
        </svg>
        <span>780-555-0142</span>
      </div>
      <div class="line">
        <svg viewBox="0 0 16 16" aria-label="Fax" role="img">
          <rect x="3" y="1.5" width="10" height="13" fill="none" stroke="#000" stroke-width="1.2"/>
          <path d="M5 5h6M5 7.5h6M5 10h6" stroke="#000" stroke-width="1"/>
        </svg>
        <span>780-555-0187</span>
      </div>
    </div>

    <div class="brand-mark">
      <span class="brand-dot"></span>
      <span>Stonelynk Co</span>
    </div>

    <div class="contact contact-web">
      <div>dale@stonelynk.com</div>
      <div>www.stonelynk.ca</div>
    </div>
  </section>

</div>
</body>
</html>
```